Vextamine™

I need a product label for a 100 ml clear glass vial with a white, blue or red crimp top . The label dimensions are 2" x 6". I am attaching my rough draft, as well as some other art work that might help the designer have a more insight as to what I am seeking. Our printer needs the artwork to be 600x600dpi in resolution. I am open to the idea of our company logo "northbay biolabs" and the product name "VEXTAMINE™" being in chrome. This product is a site enhancement oil for bodybuilders. I prefer a more "pharma" style look over a gimmicky bodybuilder theme, BUT I am open to anyone's suggestions. After this is concluded, We also want to use the template for the remainder of our supplement line.We will obviously work with the same designer to complete the remaining 6-8 products. I am new to this so if there is anything you need from me to clarify from me, please ask :)

```html
<!DOCTYPE html>
<html lang="en">
<head>
<meta charset="utf-8">
<title>Vextamine™ Label – northbay biolabs</title>
<link href="https://fonts.googleapis.com/css2?family=Montserrat:wght@600;700;800&family=Fira+Sans+Condensed:wght@600;700&family=Arimo:wght@400;700&display=swap" rel="stylesheet">
<style>
  :root{
    --navy:#262a7a;
    --navy-deep:#1f2470;
    --red:#e41d26;
    --red-deep:#a51a20;
    --ink:#111;
    --paper:#fff;
    --page:#eeeeee;
    --mist:#dedfe2;
  }
  *{box-sizing:border-box;margin:0;padding:0}
  html,body{width:1200px;height:1200px;overflow:hidden}
  body{background:var(--page);font-family:"Arimo",Arial,sans-serif;color:var(--ink);position:relative}

  /* ---------- flat label ---------- */
  .label{position:absolute;left:40px;top:60px;width:1120px;height:372px;background:var(--paper);overflow:hidden}
  .label-backdrop{position:absolute;left:230px;top:0;width:660px;height:372px;
    background:radial-gradient(ellipse at 45% 35%,#c9cacf 0%,#e2e3e6 45%,rgba(255,255,255,0) 75%)}

  .usage{position:absolute;left:42px;top:38px;width:240px;font-size:8.2px;line-height:1.38;text-align:justify}
  .usage p{margin-bottom:9px}
  .usage b{font-weight:700}
  .disclaimer{position:absolute;left:42px;top:258px;width:197px;border:1px solid #222;padding:2px 3px;font-size:6.2px;font-weight:700;line-height:1.3}
  .distributor{position:absolute;left:43px;top:308px;font-family:"Fira Sans Condensed",sans-serif;font-weight:600;font-size:11px;line-height:1.4}

  .brand{position:absolute;left:430px;top:22px;display:flex;align-items:center;gap:10px}
  .brand-name{font-family:"Montserrat",sans-serif;font-weight:800;color:var(--red-deep);font-size:34px;line-height:.95;letter-spacing:.5px}
  .brand-dot{width:14px;height:14px;border-radius:50%;background:var(--navy);align-self:flex-start;margin-top:6px}

  .product-plate{position:absolute;left:371px;top:127px;width:377px;height:86px;background:var(--navy-deep);border-radius:4px;text-align:center;color:#fff}
  .product-name{font-family:"Montserrat",sans-serif;font-weight:800;font-size:45px;letter-spacing:1px;line-height:1;margin-top:7px;color:#e6e7ea}
  .product-name sup{font-size:14px;font-weight:600;vertical-align:top;position:relative;top:4px}
  .product-grade{font-family:"Montserrat",sans-serif;font-weight:600;font-size:17px;letter-spacing:.6px;margin-top:4px}

  .claims{position:absolute;left:380px;top:228px;width:360px;list-style:none;font-family:"Arimo",sans-serif;font-weight:700;font-size:21px;color:var(--navy);text-align:center;line-height:27px}
  .claims li{display:flex;align-items:center;justify-content:center;gap:6px}
  .claims svg{width:20px;height:20px;flex:none}

  .contents-band{position:absolute;left:246px;top:327px;width:650px;height:45px;
    background:linear-gradient(90deg,rgba(228,29,38,0) 0%,var(--red) 16%,var(--red) 84%,rgba(228,29,38,0) 100%);
    display:flex;align-items:center;justify-content:center;color:#fff;font-family:"Fira Sans Condensed",sans-serif;font-weight:700;font-size:17px;gap:12px}

  .facts{position:absolute;left:839px;top:36px;width:240px;border:1px solid #111;padding:2px 4px 1px;font-size:9.5px;line-height:1.25}
  .facts h2{font-family:"Arimo",sans-serif;font-weight:700;font-size:22px;line-height:1.05}
  .facts .serving{border-bottom:4px solid #111;padding-bottom:2px}
  .facts .head{font-size:7px;border-bottom:1px solid #111;padding:2px 0}
  .facts table{width:100%;border-collapse:collapse}
  .facts td{padding:0;vertical-align:top;border-bottom:1px solid #111}
  .facts td.amt{text-align:right;white-space:nowrap;padding-right:6px}
  .facts td.dv{text-align:right;width:8px}
  .facts .foot{padding-top:1px}
  .facts i{font-style:italic}
  .other{position:absolute;left:839px;top:262px;width:240px;font-size:8.3px;line-height:1.2;text-align:justify}
  .other p{margin-bottom:2px}
  .other .caps{font-weight:700;text-transform:uppercase}
  .other .gap{margin-top:14px}

  /* ---------- logo lockups ---------- */
  .lockup{position:absolute;top:470px;width:550px;height:680px;display:flex;align-items:center;justify-content:center}
  .lockup-light{left:40px;background:var(--paper)}
  .lockup-dark{left:610px;background:var(--red)}
  .lockup .brand-name{font-size:74px}
  .lockup .brand-dot{width:28px;height:28px;margin-top:12px}
  .lockup-dark .brand-name{color:#fff}
  .lockup-dark .brand-dot{background:#fff}
  .lockup-inner{display:flex;gap:18px}
</style>
</head>
<body>

<section class="label" aria-label="Vextamine product label">
  <div class="label-backdrop" role="img" aria-label="Soft grey microscopic cell imagery behind the brand area"></div>

  <div class="usage">
    <p><b>SUGGESTED USE:</b> 1 capsule taken 1 to 2 times daily preferably with meals or as directed by a healthcare professional.</p>
    <p><b>CAUTION:</b> Do not exceed recommended dose. St. John's Wort may contribute to photosensitivity resulting in skin irritation and redness in persons exposed to strong sunlight or tanning booths. Avoid use in patients at risk of bleeding, taking anticoagulants, or with clotting disorders, based on case reports of bleeding. Discontinue use 2-3 weeks prior to some surgical and dental procedures due to increased risk of bleeding. Avoid use in couples who are trying to conceive, based on theoretical reduction of fertility. Pregnant or nursing mothers, children under 18, individuals with history of seizure, taking MAO inhibiting drugs, or with a known medical condition should consult a physician before using this or any dietary supplement. This product is manufactured and packaged in a facility which may also process milk, soy, wheat, egg, peanuts, tree nuts, fish and crustacean shellfish.</p>
  </div>
  <div class="disclaimer">†These statements have not been evaluated by the Food &amp; Drug Administration. This product is not intended to diagnose, treat, cure or prevent any disease.</div>
  <div class="distributor">Distributed by:<br>Company Name<br>Full Address and Phone</div>

  <div class="brand">
    <div class="brand-name">northbay<br>biolabs</div>
    <span class="brand-dot"></span>
  </div>

  <div class="product-plate">
    <div class="product-name">VEXTAMINE<sup>TM</sup></div>
    <div class="product-grade">PHARMACEUTICAL GRADE</div>
  </div>

  <ul class="claims">
    <li><svg viewBox="0 0 20 20"><circle cx="10" cy="10" r="8.5" fill="none" stroke="#e41d26" stroke-width="2"/><path d="M5.5 10.2l3 3 6-6.4" fill="none" stroke="#e41d26" stroke-width="2.2"/></svg>MUSCLE VOLUMIZATION</li>
    <li><svg viewBox="0 0 20 20"><circle cx="10" cy="10" r="8.5" fill="none" stroke="#e41d26" stroke-width="2"/><path d="M5.5 10.2l3 3 6-6.4" fill="none" stroke="#e41d26" stroke-width="2.2"/></svg>SITE ENHANCMENT</li>
    <li><svg viewBox="0 0 20 20"><circle cx="10" cy="10" r="8.5" fill="none" stroke="#e41d26" stroke-width="2"/><path d="M5.5 10.2l3 3 6-6.4" fill="none" stroke="#e41d26" stroke-width="2.2"/></svg>JOINT THERAPY</li>
  </ul>

  <div class="contents-band"><span>Contents : 100ml</span><span>|</span><span>Shake Before Each Use.</span></div>

  <div class="facts">
    <h2>Supplement Facts</h2>
    <div class="serving">Serving Size 1 Capsule<br>Servings Per Container: 30</div>
    <div class="head">Amt Per Serv. %DV/RDI</div>
    <table>
      <tr><td><i>Ginkgo biloba</i> Leaf (24% extract)</td><td class="amt">50mg</td><td class="dv">*</td></tr>
      <tr><td>Phosphatidylserine 4% Complex (consisting of Lecithin and Phosphatidylserine)</td><td class="amt">125mg</td><td class="dv">*</td></tr>
      <tr><td>N-Acetyl L-Carnitine HCl</td><td class="amt">50mg</td><td class="dv">*</td></tr>
      <tr><td>St. John's Wort (0.3% extract) (flower heads)</td><td class="amt">250mg</td><td class="dv">*</td></tr>
      <tr><td>L-Glutamine</td><td class="amt">150mg</td><td class="dv">*</td></tr>
      <tr><td><i>Bacopa monnieri</i> Leaf Extract (20% bacosides)</td><td class="amt">120mg</td><td class="dv">*</td></tr>
      <tr><td>Vinpocetine (seeds)</td><td class="amt">2mg</td><td class="dv">*</td></tr>
      <tr><td>Huperzine-A (aerial plant)</td><td class="amt">10mcg</td><td class="dv">*</td></tr>
    </table>
    <div class="foot">*Daily Value not established.</div>
  </div>

  <div class="other">
    <p><b>Other ingredients:</b> Gelatin (bovine), microcrystalline cellulose, vegetable magnesium stearate, and silicon dioxide.</p>
    <p class="caps">Allergen warning: contains soy (lecithin).</p>
    <p class="caps gap">Keep out of the reach of children.<br>Do not use if safety seal is damaged or missing. Store in a cool, dry place.</p>
  </div>
</section>

<section class="lockup lockup-light" aria-label="Brand mark on white">
  <div class="brand lockup-inner" style="position:static">
    <div class="brand-name">northbay<br>biolabs</div>
    <span class="brand-dot"></span>
  </div>
</section>

<section class="lockup lockup-dark" aria-label="Brand mark reversed on red">
  <div class="brand lockup-inner" style="position:static">
    <div class="brand-name">northbay<br>biolabs</div>
    <span class="brand-dot"></span>
  </div>
</section>

</body>
</html>
```